Innovative Freezer Label Design

Create a versatile and innovative freezer label design with universal appeal, suitable for different functionalities. The design should cater to a diverse audience, including those who freeze meals for meal prepping, batch cooking, and the restaurant industry. Our vision is a visually striking and distinctive design that embodies simplicity.

Example "our current labels feature essential details like "Contents" and "Date." We recognize these as crucial points of information. Currently, the challenge lies in creating various labels for different marketplaces, considering language barriers. A proposed solution involves the integration of universal icons to replace specific words, promoting practicality for international sales."

Kindly note that design concepts should not be restricted to our current product, brand guideline, logo, or the provided example.

Our goal is not only product differentiation but also increased sales through a blend of functionality and aesthetics.

The following are examples of freezer labels designs. Kindly do not restrict your designs to the examples. The designs must be universal (for language barrier purposes)

Examples:
https://www.tackvora.co.uk/pin/5827164039281736401/
https://www.tackvora.co.uk/pin/5827164039281736405/
https://www.tackvora.co.uk/pin/5827164039281736394/
https://www.tackvora.co.uk/pin/5827164039281736308/
https://www.tackvora.co.uk/pin/5827164039281797750/

Please reach out if you have any questions.

Thank you

```html
<!DOCTYPE html>
<html lang="en">
<head>
<meta charset="utf-8">
<title>Freezer Label – Contents &amp; Date</title>
<link rel="stylesheet" href="https://fonts.googleapis.com/css2?family=Roboto:wght@500&display=swap">
<style>
  :root {
    --canvas-bg: #f2f2f0;
    --label-pattern-light: #d9d9d9;
    --label-pattern-mid: #bdbdbd;
    --label-pattern-dark: #8a8a8a;
    --label-card: #f7f7f7;
    --ink: #2b2b2b;
    --rule: #555555;
  }
  html, body {
    margin: 0;
    padding: 0;
    width: 1200px;
    height: 1200px;
    overflow: hidden;
    background: var(--canvas-bg);
    font-family: "Roboto", sans-serif;
  }
  .canvas {
    position: relative;
    width: 1200px;
    height: 1200px;
  }
  .freezer-label {
    position: absolute;
    left: 100px;
    top: 306px;
    width: 1000px;
    height: 587px;
    border-radius: 18px;
    overflow: hidden;
    box-shadow: 0 2px 6px rgba(0,0,0,0.12);
  }
  .label-pattern {
    position: absolute;
    inset: 0;
    background: linear-gradient(135deg, var(--label-pattern-light) 0%, var(--label-pattern-mid) 55%, var(--label-pattern-dark) 100%);
  }
  .label-card {
    position: absolute;
    left: 60px;
    top: 60px;
    width: 880px;
    height: 467px;
    background: var(--label-card);
    border-radius: 14px;
    display: flex;
    flex-direction: column;
    justify-content: center;
    gap: 56px;
    padding: 0 70px;
    box-sizing: border-box;
  }
  .field {
    display: flex;
    align-items: flex-end;
    height: 80px;
  }
  .field-icon {
    width: 80px;
    height: 80px;
    flex: none;
  }
  .field-icon * {
    fill: none;
    stroke: var(--ink);
    stroke-width: 5;
    stroke-linecap: round;
    stroke-linejoin: round;
  }
  .field-rule {
    flex: 1;
    margin-left: 40px;
    margin-bottom: 6px;
    border-bottom: 3px solid var(--rule);
  }
</style>
</head>
<body>
  <main class="canvas">
    <section class="freezer-label">
      <div class="label-pattern" role="img" aria-label="Grey fruit and dot pattern border of the label"></div>
      <div class="label-card">
        <div class="field field-contents">
          <svg class="field-icon" viewBox="0 0 80 80" role="img" aria-label="Contents">
            <rect x="10" y="30" width="60" height="40" rx="6"/>
            <rect x="6" y="18" width="68" height="12" rx="4"/>
            <line x1="30" y1="10" x2="50" y2="10"/>
            <line x1="40" y1="10" x2="40" y2="18"/>
          </svg>
          <span class="field-rule"></span>
        </div>
        <div class="field field-date">
          <svg class="field-icon" viewBox="0 0 80 80" role="img" aria-label="Date">
            <rect x="8" y="14" width="64" height="58" rx="6"/>
            <line x1="8" y1="30" x2="72" y2="30"/>
            <line x1="24" y1="6" x2="24" y2="20"/>
            <line x1="56" y1="6" x2="56" y2="20"/>
            <line x1="22" y1="44" x2="26" y2="44"/>
            <line x1="38" y1="44" x2="42" y2="44"/>
            <line x1="54" y1="44" x2="58" y2="44"/>
            <line x1="22" y1="58" x2="26" y2="58"/>
            <line x1="38" y1="58" x2="42" y2="58"/>
          </svg>
          <span class="field-rule"></span>
        </div>
      </div>
    </section>
  </main>
</body>
</html>
```